Corwin Halvey Golf Instruction

I need a web design for a golf instruction website. My goal is to gain more exposure through this site. I want this site to be a source for golf knowledge and instruction by providing instructional videos and instructional literature. I want the site to have colors navy blue(tulsa ravens blue) and silver. I am also open to other color schemes. The main website to imitate is deklanmorrowby.example. I want tabs/links at the top of the site that read: Home, About, Video Instruction, Instruction, and Golf Blog. Other sites to reference are Pell Vostrand Golf and truearcbirdieplay.example. A main feature that must be included is online video lessons like on pellvostrand.example. I have software that provides me the ability to take a video of a golf swing and record a voice video lesson. Reference the example video on pellvostrand.example.

The main goal for this web design is to have an "outline" in place so that I can go back and input the videos and literature.

Reason: I need more time to wait for changes. I like all the designs.

Target Market(s)

My target market is golfer of all ages and abilities: juniors, adults, men, and women.

Industry/Entity Type

Software

Requirements
Must have
• Capability to input videos and literature onto the site.
"Lead Instructor at Marlpit Golf Club" title.
A very visible "Marlpit Golf Club" logo.
Facebook, Twitter, and YouTube quicklinks.

```html
<!DOCTYPE html>
<html lang="en">
<head>
<meta charset="utf-8">
<title>Kestrel Golf – Corwin Halvey Golf Instruction</title>
<link rel="stylesheet" href="https://fonts.googleapis.com/css2?family=Archivo+Narrow:wght@400;600;700&family=Open+Sans:wght@400;600&display=swap">
<style>
:root{
  --navy:#0d4a78;
  --navy-dark:#083a60;
  --ink:#444;
  --green:#7cad1c;
  --green-bar:#8dba10;
  --orange:#f39a12;
  --yellow:#f2c500;
  --sky:#7fb2dd;
  --grass:#8fbf3a;
  --white:#fff;
  --link:#4f8a12;
  --blue-temp:#2a9ad6;
}
*{box-sizing:border-box;margin:0;padding:0}
html,body{width:852px;height:1200px;overflow:hidden}
body{
  position:relative;
  font-family:"Open Sans",sans-serif;
  color:var(--ink);
  background:linear-gradient(180deg,#5e95cf 0%,#9cc3e6 22%,#6f9a4a 42%,#98c443 60%,#8bbb34 100%);
}
.backdrop{position:absolute;inset:0}
.page{position:absolute;left:121px;top:0;width:610px;height:1200px}
.brand{position:absolute;left:24px;top:50px;font-family:"Archivo Narrow",sans-serif;font-weight:700;font-size:50px;color:var(--navy);letter-spacing:1px}
.brand-dot{display:inline-block;width:18px;height:18px;border-radius:50%;background:var(--navy);margin-right:8px;vertical-align:middle}
.club{position:absolute;left:300px;top:40px;width:260px;text-align:center;font-family:"Archivo Narrow",sans-serif;font-weight:700;font-size:28px;color:var(--white)}
.club-title{position:absolute;left:275px;top:96px;width:310px;text-align:center;font-family:"Archivo Narrow",sans-serif;font-weight:700;font-size:20px;color:var(--white)}
.nav{position:absolute;left:0;top:148px;width:610px;height:36px;background:linear-gradient(180deg,#17608f,var(--navy-dark));display:flex;align-items:center;font-family:"Archivo Narrow",sans-serif;font-size:13px;color:var(--white)}
.nav a{color:var(--white);text-decoration:none;padding:0 12px;height:36px;line-height:36px}
.nav a:first-child{padding-left:22px}
.nav a.active{background:#0a4068}
.follow{margin-left:auto;display:flex;align-items:center;gap:4px;padding-right:18px}
.follow span{margin-right:4px}
.follow i{display:block;width:15px;height:15px;border-radius:50%;background:var(--white)}
.hero{position:absolute;left:0;top:188px;width:610px;height:266px;background:linear-gradient(180deg,#3f6b2e 0%,#5f8a35 35%,#87b23a 70%,#6b9a2c 100%)}
.hero-box{position:absolute;left:56px;top:54px;width:262px;height:140px;background:rgba(255,255,255,.22);padding:10px 12px}
.hero-box h1{font-family:"Archivo Narrow",sans-serif;font-weight:400;font-size:24px;line-height:30px;color:var(--white)}
.hero-box p{font-size:7px;line-height:10px;color:var(--white);margin-top:6px}
.btn{position:absolute;top:107px;height:22px;line-height:22px;padding:0 14px;font-family:"Archivo Narrow",sans-serif;font-size:11px;color:var(--white)}
.btn-more{left:12px;background:var(--green)}
.btn-tour{left:105px;background:var(--orange)}
.arrow{position:absolute;top:94px;width:30px;height:42px;background:rgba(255,255,255,.85);display:flex;align-items:center;justify-content:center}
.arrow-left{left:0;border-radius:0 4px 4px 0}
.arrow-right{right:0;border-radius:4px 0 0 4px}
.tiles{position:absolute;left:0;top:457px;width:610px;height:120px;display:flex;gap:2px}
.tile{position:relative;flex:1}
.tile-photo{position:absolute;inset:0}
.tile-label{position:absolute;left:0;bottom:0;width:100%;height:25px;display:flex;align-items:center;gap:6px;padding-left:12px;font-family:"Archivo Narrow",sans-serif;font-size:11px;color:var(--white)}
.label-blue{background:var(--navy)}
.label-green{background:var(--green-bar)}
.label-yellow{background:var(--yellow)}
.content{position:absolute;left:0;top:577px;width:610px;height:569px;background:var(--white)}
.quote{position:absolute;left:12px;top:13px;font-family:"Archivo Narrow",sans-serif;font-size:18px;color:var(--navy)}
.feature-video{position:absolute;left:12px;top:47px;width:221px;height:133px;background:linear-gradient(135deg,#3d6a24,#7ea047 60%,#2f4e1d)}
.play{position:absolute;left:86px;top:43px}
.body-text{font-size:10.5px;line-height:21px;color:var(--ink)}
.feature-text{position:absolute;left:243px;top:44px;width:354px}
.read-more{position:absolute;font-family:"Archivo Narrow",sans-serif;font-weight:600;font-size:11px;color:var(--link);display:flex;align-items:center;gap:4px}
.story-photo{position:absolute;left:12px;width:131px;height:108px}
.story-title{position:absolute;left:151px;font-family:"Archivo Narrow",sans-serif;font-size:16px;color:var(--navy)}
.story-text{position:absolute;left:151px;width:245px}
.side-head{position:absolute;left:415px;width:182px;height:24px;background:var(--navy);color:var(--white);font-family:"Archivo Narrow",sans-serif;font-size:14px;display:flex;align-items:center;gap:6px;padding-left:10px;box-shadow:0 4px 5px rgba(0,0,0,.15)}
.forecast{position:absolute;left:415px;top:260px;width:182px;display:flex;justify-content:space-between}
.day{width:58px;text-align:center}
.day-name{font-size:11px;font-weight:600;color:var(--green);margin-top:2px}
.temps{font-size:10px;color:var(--ink)}
.temps b{font-weight:400;color:var(--blue-temp)}
.review{position:absolute;left:415px;width:182px}
.avatar{position:absolute;left:0;top:0;width:58px;height:58px;background:linear-gradient(180deg,#8a6d55,#3c3a3a)}
.review-name{position:absolute;left:67px;top:10px;font-size:10px;font-weight:600;color:var(--green);white-space:nowrap}
.review-text{position:absolute;left:67px;top:26px;width:115px;font-size:10.5px;line-height:19px}
.footer{position:absolute;left:0;top:1162px;width:610px;text-align:center;font-family:"Archivo Narrow",sans-serif;font-weight:700;font-size:11px;color:var(--white)}
</style>
</head>
<body>
<div class="backdrop" role="img" aria-label="Blurred golf course backdrop with trees, sky and a gloved hand placing a ball"></div>

<div class="page">
  <header>
    <div class="brand"><span class="brand-dot"></span>Kestrel Golf</div>
    <div class="club">Marlpit Golf Club</div>
    <div class="club-title">Lead Instructor at Marlpit Golf Club</div>
  </header>

  <nav class="nav">
    <a href="#">Home</a>
    <a href="#">About</a>
    <a href="#" class="active">Video Instructions</a>
    <a href="#">Golf Blog</a>
    <div class="follow"><span>Follow us on:</span><i aria-label="Social link one"></i><i aria-label="Social link two"></i><i aria-label="Social link three"></i></div>
  </nav>

  <section class="hero" role="img" aria-label="Golfer's gloved hand setting a ball on a tee beside an iron">
    <div class="arrow arrow-left"><svg width="10" height="16" viewBox="0 0 10 16"><path d="M8 2 2 8l6 6" fill="none" stroke="#bbb" stroke-width="2"/></svg></div>
    <div class="hero-box">
      <h1>Learning a Consistent<br>Golf Swing</h1>
      <p>Lorem ipsum dolor sit amet, consectetur adipiscing elit. Nullam nec mauris est. Ut justo odio, iaculis in eleifend sed, pharetra in dui. Maecenas et nisi sit amet dolor</p>
      <a class="btn btn-more">Learn More</a>
      <a class="btn btn-tour">Take a Tour</a>
    </div>
    <div class="arrow arrow-right"><svg width="10" height="16" viewBox="0 0 10 16"><path d="M2 2l6 6-6 6" fill="none" stroke="#bbb" stroke-width="2"/></svg></div>
  </section>

  <section class="tiles">
    <div class="tile">
      <div class="tile-photo" role="img" aria-label="Golf bag with clubs on grass" style="background:linear-gradient(135deg,#5a8a2a,#2d3b22 70%)"></div>
      <div class="tile-label label-blue"><svg width="13" height="13" viewBox="0 0 14 14"><circle cx="7" cy="7" r="4.5" fill="none" stroke="#fff" stroke-width="3" stroke-dasharray="2.2 1.3"/><circle cx="7" cy="7" r="2" fill="#fff"/></svg>Our Golf Gear</div>
    </div>
    <div class="tile">
      <div class="tile-photo" role="img" aria-label="Golfer playing out of a bunker" style="background:linear-gradient(135deg,#9a9a9a,#d2d2d2 50%,#4b5a7a)"></div>
      <div class="tile-label label-green"><svg width="14" height="11" viewBox="0 0 14 11"><path d="M1 1h5l1 1 1-1h5v9H8l-1 1-1-1H1z" fill="#fff"/></svg>Online Courses</div>
    </div>
    <div class="tile">
      <div class="tile-photo" role="img" aria-label="Golfer finishing a swing in front of a city skyline" style="background:linear-gradient(180deg,#3d7fc7,#8ab6df 60%,#6d8e3a)"></div>
      <div class="tile-label label-yellow"><svg width="10" height="14" viewBox="0 0 10 14"><circle cx="5" cy="5" r="4.5" fill="#fff"/><rect x="3" y="9" width="4" height="4" fill="#fff"/></svg>To perfection</div>
    </div>
  </section>

  <main class="content">
    <h2 class="quote">"A great golf course is just the beginning..."</h2>
    <div class="feature-video" role="img" aria-label="Video lesson: golfer following through on a swing">
      <svg class="play" width="50" height="50" viewBox="0 0 50 50"><circle cx="25" cy="25" r="24" fill="#2aa3e6" stroke="#fff" stroke-width="2"/><path d="M19 14l16 11-16 11z" fill="#fff"/></svg>
    </div>
    <p class="body-text feature-text">If you're chasing that elusive river cod, Waterskiing, Boating, Fishing, relaxing on a houseboat or sunbaking on our golden beaches, Benthill is the perfect place to base yourself for a Larrow River break. We are central to all the Larrow attractions as well as having over 350 golf holes within an hours drive. Social golfers are welcome here 7 days a week.</p>
    <a class="read-more" style="left:523px;top:167px">READ MORE <svg width="11" height="11" viewBox="0 0 12 12"><circle cx="6" cy="6" r="6" fill="var(--link)"/><path d="M3 6h5M6 3.5 8.5 6 6 8.5" fill="none" stroke="#fff" stroke-width="1.6"/></svg></a>

    <div class="story-photo" style="top:213px;background:linear-gradient(180deg,#6a8f3f,#8bb84d)" role="img" aria-label="Golfers and caddies walking the fairway"></div>
    <h3 class="story-title" style="top:221px">Watch Wren Tallow</h3>
    <p class="body-text story-text" style="top:242px">There's so much to do on the beautiful Larrow River. Discover Benthill's 36 Hole Championship Golf Course, glorious golden sandy beach-</p>
    <a class="read-more" style="left:321px;top:309px">READ MORE <svg width="11" height="11" viewBox="0 0 12 12"><circle cx="6" cy="6" r="6" fill="var(--link)"/><path d="M3 6h5M6 3.5 8.5 6 6 8.5" fill="none" stroke="#fff" stroke-width="1.6"/></svg></a>

    <div class="story-photo" style="top:358px;background:linear-gradient(135deg,#3f5b2a,#7d9a55 60%,#56733a)" role="img" aria-label="Professional golfer holding a club"></div>
    <h3 class="story-title" style="top:366px">Professional Golfer</h3>
    <p class="body-text story-text" style="top:386px">There's so much to do on the beautiful Larrow River. Discover Benthill's 36 Hole Championship Golf Course, glorious golden sandy beach-</p>
    <p class="body-text story-text" style="top:454px">There's so much to do on the beautiful Larrow River. Discover Benthill's 36 Hole Championship Golf Course, glorious golden sandy beach-</p>
    <a class="read-more" style="left:321px;top:537px">READ MORE <svg width="11" height="11" viewBox="0 0 12 12"><circle cx="6" cy="6" r="6" fill="var(--link)"/><path d="M3 6h5M6 3.5 8.5 6 6 8.5" fill="none" stroke="#fff" stroke-width="1.6"/></svg></a>

    <div class="side-head" style="top:220px"><svg width="13" height="13" viewBox="0 0 14 14"><circle cx="7" cy="7" r="3" fill="#fff"/><path d="M7 0v3M7 11v3M0 7h3M11 7h3M2 2l2 2M10 10l2 2M2 12l2-2M10 4l2-2" stroke="#fff" stroke-width="1.5"/></svg>Weather</div>
    <div class="forecast">
      <div class="day">
        <svg width="48" height="32" viewBox="0 0 48 32"><circle cx="18" cy="12" r="8" fill="#f5b800"/><ellipse cx="28" cy="22" rx="17" ry="8" fill="#e9eef2"/><circle cx="30" cy="15" r="8" fill="#f1f4f6"/></svg>
        <div class="day-name">Saturday</div><div class="temps"><b>17 C</b> - 9 C</div>
      </div>
      <div class="day">
        <svg width="48" height="32" viewBox="0 0 48 32"><circle cx="18" cy="12" r="8" fill="#f5b800"/><ellipse cx="28" cy="20" rx="17" ry="7" fill="#e9eef2"/><circle cx="30" cy="14" r="7" fill="#f1f4f6"/><path d="M24 28l-1 3M31 28l-1 3" stroke="#2a9ad6" stroke-width="2"/></svg>
        <div class="day-name">Sunday</div><div class="temps"><b>9 C</b> - 5 C</div>
      </div>
      <div class="day">
        <svg width="48" height="32" viewBox="0 0 48 32"><circle cx="18" cy="12" r="8" fill="#f5b800"/><ellipse cx="28" cy="22" rx="17" ry="8" fill="#e9eef2"/><circle cx="30" cy="15" r="8" fill="#f1f4f6"/></svg>
        <div class="day-name">Monday</div><div class="temps"><b>13C</b> - 7 C</div>
      </div>
    </div>

    <div class="side-head" style="top:363px"><svg width="13" height="12" viewBox="0 0 14 12"><path d="M1 1h12v7H6l-4 3V8H1z" fill="#fff"/></svg>What they say</div>
    <div class="review" style="top:404px">
      <div class="avatar" role="img" aria-label="Portrait of reviewer Milo Garrand"></div>
      <div class="review-name">Milo GARRAND</div>
      <p class="review-text">"It's just AWSOME. Proffesional Course."</p>
    </div>
    <div class="review" style="top:471px">
      <div class="avatar" role="img" aria-label="Portrait of reviewer Stefan Korrow"></div>
      <div class="review-name">Stefan KORROW</div>
      <p class="review-text">"I love this classe. I could be pro!</p>
    </div>
  </main>

  <footer class="footer">Kestrel Golf Club 2012 Copyright!All rights Reserved!</footer>
</div>
</body>
</html>
```